Design concept for BrightKestrel.com Support Page

We are about to launch a new support page for our www.brightkestrel.com service for photographers and visual artists. The service provides media management, cloud storage, promotional and secure distribution to our members.

The support page will include FAQs and video tutorials.

In particular we're looking for a header for this page that suggests the user is in the support area of our service - so perhaps an illustration that suggests support could look nice (perhaps repair man or doctor iconography). Something to give this area of our site a different look and something that looks both cool and friendly.

Currently the page looks distinctly sparse and undesigned (see attached screenshot) - something that could be remedied, we feel, by some subtle design enhancements that we can implement using CSS.

```html
<!DOCTYPE html>
<html lang="en">
<head>
<meta charset="utf-8">
<title>BrightKestrel.com – Frequently Asked Questions</title>
<link rel="stylesheet" href="https://fonts.googleapis.com/css2?family=Open+Sans:ital,wght@0,300;0,400;0,600;0,700;1,300;1,400&display=swap">
<style>
:root{
  --ink:#111111;
  --header-text:#333333;
  --orange:#f4a623;
  --tile:#000000;
  --white:#ffffff;
  --footer:#050505;
  --footer-link:#c9c9c9;
  --footer-muted:#7a7a7a;
  --rule:#cfcfcf;
}
*{margin:0;padding:0;box-sizing:border-box}
html,body{width:1040px;height:1200px;overflow:hidden;background:var(--white)}
body{position:relative;font-family:"Open Sans",Arial,sans-serif;color:var(--ink)}

.site-header{position:absolute;left:0;top:0;width:1040px;height:56px}
.brand-name{position:absolute;left:106px;top:13px;font-weight:400;font-size:20px;line-height:28px;color:var(--header-text);white-space:nowrap}
.header-divider{position:absolute;left:314px;top:10px;width:1px;height:34px;background:var(--rule)}
.page-label{position:absolute;left:323px;top:17px;font-size:16.5px;font-weight:400;color:var(--header-text);display:flex;align-items:center;gap:9px;white-space:nowrap}
.page-label svg{display:block}

.hero{position:absolute;left:3px;top:56px;width:1037px;height:432px;
  background:radial-gradient(ellipse at 70% 75%,#6a6a6a 0%,#3a3b3d 40%,#24272b 75%,#1c1f24 100%)}
.hero-title{position:absolute;left:0;top:124px;width:1040px;text-align:center;
  font-style:italic;font-weight:300;font-size:55px;line-height:64px;color:var(--white);letter-spacing:-0.5px}
.search-panel{position:absolute;left:245px;top:219px;width:551px;height:52px;background:rgba(150,150,150,.75)}
.search-input{position:absolute;left:13px;top:13px;width:441px;height:26px;background:var(--white);
  font-style:italic;font-size:11.5px;line-height:26px;color:#b3b3b3;padding-left:11px}
.search-button{position:absolute;left:454px;top:13px;width:84px;height:26px;background:var(--orange);
  font-style:italic;font-size:11.5px;line-height:26px;color:var(--white);text-align:center}

.section-title{position:absolute;left:104px;top:516px;font-weight:300;font-size:33px;line-height:44px;color:var(--ink)}

.tile{position:absolute;background:var(--tile);color:var(--white);text-align:center}
.tile svg{position:absolute;left:50%;transform:translateX(-50%)}
.tile-small{width:195px;height:195px}
.tile-small svg{top:33px}
.tile-small .tile-label{position:absolute;left:0;width:100%;top:155px;font-size:16.5px;line-height:20px}
.tile-featured{left:104px;top:586px;width:407px;height:406px;background:var(--orange);color:var(--ink)}
.tile-featured svg{top:65px}
.tile-featured .tile-label{position:absolute;left:0;width:100%;top:213px;font-size:21px;line-height:28px;font-weight:400}
.tile-featured .tile-text{position:absolute;left:60px;width:287px;top:252px;font-size:12px;line-height:16.5px;font-weight:300;text-align:center}

.site-footer{position:absolute;left:0;top:1090px;width:1040px;height:110px;background:var(--footer);border-top:4px solid #1e1e1e}
.footer-links{position:absolute;top:25px;left:0;width:1040px;text-align:center;font-size:9.5px;font-weight:600;color:var(--footer-link)}
.footer-links span{margin:0 6px}
.copyright{position:absolute;top:56px;left:0;width:1040px;text-align:center;font-size:9.5px;font-weight:700;color:var(--white)}
.powered{position:absolute;top:69px;left:0;width:1040px;text-align:center;font-size:9px;color:var(--footer-muted)}
</style>
</head>
<body>

<header class="site-header">
  <div class="brand-name">BrightKestrel.com</div>
  <div class="header-divider"></div>
  <div class="page-label">Frequently Asked Questions
    <svg width="22" height="22" viewBox="0 0 22 22" aria-hidden="true"><path d="M2 2h18v13H9l-4 4v-4H2z" fill="none" stroke="#f4a623" stroke-width="1.5" stroke-linejoin="round"/><path d="M6 7h10M6 10h8" stroke="#f4a623" stroke-width="1.3"/></svg>
  </div>
</header>

<section class="hero" role="img" aria-label="Black and white photograph of a photographer's hands holding a compact rangefinder camera"></section>
<h1 class="hero-title">We’ve got all the answers...</h1>
<div class="search-panel">
  <div class="search-input">What’s your question?</div>
  <div class="search-button">Search</div>
</div>

<h2 class="section-title">Video Tutorials</h2>

<div class="tile tile-featured">
  <svg width="138" height="138" viewBox="0 0 138 138" aria-hidden="true"><circle cx="69" cy="69" r="66" fill="none" stroke="#000" stroke-width="4"/><path d="M54 45v47l40-23.5z" fill="#000"/></svg>
  <div class="tile-label">Publishing Files</div>
  <p class="tile-text">Lorem ipsum dolor sit amet, consectetur vitas adipiscing. molestie dui vitae egestas euismod. Vivamus luctus orci sit amet tincidunt euismod</p>
</div>

<div class="tile tile-small" style="left:529px;top:586px">
  <svg width="96" height="96" viewBox="0 0 96 96" aria-hidden="true"><circle cx="48" cy="48" r="45" fill="none" stroke="#fff" stroke-width="3.5"/><path d="M37 32v32l28-16z" fill="#fff"/></svg>
  <div class="tile-label">Creating Galleries</div>
</div>
<div class="tile tile-small" style="left:741px;top:587px">
  <svg width="96" height="96" viewBox="0 0 96 96" aria-hidden="true"><circle cx="48" cy="48" r="45" fill="none" stroke="#fff" stroke-width="3.5"/><path d="M37 32v32l28-16z" fill="#fff"/></svg>
  <div class="tile-label">Creating Portfolios</div>
</div>
<div class="tile tile-small" style="left:529px;top:798px">
  <svg width="96" height="96" viewBox="0 0 96 96" aria-hidden="true"><circle cx="48" cy="48" r="45" fill="none" stroke="#fff" stroke-width="3.5"/><path d="M37 32v32l28-16z" fill="#fff"/></svg>
  <div class="tile-label">Managing Files</div>
</div>
<div class="tile tile-small" style="left:741px;top:798px">
  <svg width="96" height="96" viewBox="0 0 96 96" aria-hidden="true"><circle cx="48" cy="48" r="45" fill="none" stroke="#fff" stroke-width="3.5"/><path d="M37 32v32l28-16z" fill="#fff"/></svg>
  <div class="tile-label">Managing Folders</div>
</div>

<footer class="site-footer">
  <div class="footer-links">Home<span>•</span>Contact Us<span>•</span>Affiliate Program<span>•</span>Privacy Policy<span>•</span>Site Terms and Conditions<span>•</span>About Us</div>
  <div class="copyright">© Copyright 2014 Harbourline Images Pte Ltd. All rights reserved.</div>
  <div class="powered">Powered by BrightKestrel.com</div>
</footer>

</body>
</html>
```